FIRE ALARM INSTALLATION & MAINTENANCE COMPANY NEEDS A BUSINESS CARD DESIGN

WE NEED A BUSINESS CARD DESIGN FOR AN EXISTING COMPANY IN QUEENSLAND AUSTRALIA. WE DESIGN & INSTALL FIRE DETECTION AND EMERGENCY WARNING SYSTEMS.
WE OFFER COMPREHENSIVE MAINTEANCE ON ALL FIRE PREVENTION SYSTEMS. OUR EXISTING LOGO IS ATTACHED. WE WOULD LIKE TO SEE A FRESH CREATIVE LOOK AND THINK THAT PERHAPS HAVING A BLACK OR SLATE BACKGROUND WILL ENHANCE THE COLOURS OF THE LOGO MORE. WE NEED PROVISION FOR NAMES, MOBILE PHONE NUMBERS AND WEB THE ADDRESS.

Target Market(s)

Australian Construction Project managers,construction business owners, building owners/managers, body corporate.

Industry/Entity Type

Business

Font styles to use
Serif
Sans Serif

Requirements
Must have
• Must use the logo.
On the back side of the card it needs to have:
Installation of: Fire Detection and Emergency Warning Systems
Comprehensive maintenance of all Fire Protection and prevention equipment and systems.
24/7 on call maintenance
Nice to have
• We think that use a black or slate background would make the logo standout more.
We dont mind if the wording TECHNOLOGIES AND Marlow Alarm & Egress under the logo is moved in order to center or balance the design layout.
Should not have
• no illustrations or motifs

```html
<!DOCTYPE html>
<html lang="en">
<head>
<meta charset="utf-8">
<title>MAE Technologies – Business Card</title>
<link rel="stylesheet" href="https://fonts.googleapis.com/css2?family=Jost:wght@300;400;600&family=Oswald:wght@500&display=swap">
<style>
  :root {
    --backdrop: #b4b4b4;
    --card: #0e0e0e;
    --card-sheen: #2a2a2a;
    --ink-light: #f2f2f2;
    --ink-soft: #d6d6d6;
    --accent: #f39a1e;
    --accent-deep: #e0641c;
  }
  * { box-sizing: border-box; margin: 0; padding: 0; }
  html, body { width: 1200px; height: 646px; overflow: hidden; }
  body {
    background: var(--backdrop);
    font-family: "Jost", "Helvetica Neue", Arial, sans-serif;
    position: relative;
  }
  .card {
    position: absolute;
    top: 180px;
    width: 500px;
    height: 286px;
    background: radial-gradient(ellipse at 30% 20%, var(--card-sheen) 0%, var(--card) 60%);
    box-shadow: 0 10px 26px rgba(0,0,0,.35);
    color: var(--ink-light);
    overflow: hidden;
  }
  .card--front { left: 70px; }
  .card--back  { left: 630px; }

  /* Brand lockup */
  .brand { position: absolute; display: flex; align-items: center; gap: 12px; }
  .brand__dot { border-radius: 50%; background: var(--accent-deep); flex: none; }
  .brand__name { font-weight: 600; color: var(--ink-light); letter-spacing: .06em; line-height: 1; white-space: nowrap; }
  .brand__tagline { position: absolute; font-weight: 600; color: var(--accent); line-height: 1; white-space: nowrap; }

  .card--front .brand { left: 34px; top: 44px; }
  .card--front .brand__dot { width: 30px; height: 30px; }
  .card--front .brand__name { font-size: 22px; }
  .card--front .brand__tagline { left: 76px; top: 80px; font-size: 15px; }

  .contact { position: absolute; right: 28px; top: 48px; list-style: none; }
  .contact__item { display: flex; align-items: center; gap: 7px; font-size: 11.5px; color: var(--accent); margin-bottom: 4px; }
  .contact__icon { width: 12px; height: 12px; flex: none; }

  .person { position: absolute; left: 34px; bottom: 52px; font-weight: 300; font-size: 27px; letter-spacing: .05em; color: var(--ink-light); }

  .card--back .brand { left: 30px; top: 118px; flex-direction: column; align-items: flex-start; gap: 10px; }
  .card--back .brand__dot { width: 44px; height: 44px; }
  .card--back .brand__name { font-size: 22px; }
  .card--back .brand__tagline { left: 30px; top: 206px; font-size: 17px; }

  .services { position: absolute; right: 26px; top: 34px; width: 150px; text-align: right; font-size: 12px; line-height: 1.3; color: var(--ink-soft); }
  .services p { margin-bottom: 12px; }
  .services__callout { font-family: "Oswald", "Arial Narrow", sans-serif; font-weight: 500; color: var(--accent); font-size: 13px; letter-spacing: .02em; white-space: nowrap; }
</style>
</head>
<body>
  <section class="card card--front" aria-label="Business card front">
    <div class="brand">
      <span class="brand__dot"></span>
      <span class="brand__name">MAE TECHNOLOGIES</span>
    </div>
    <span class="brand__tagline">Marlow Alarm &amp; Egress</span>

    <ul class="contact">
      <li class="contact__item">
        <svg class="contact__icon" viewBox="0 0 12 12"><rect width="12" height="12" rx="2" fill="var(--accent)"/><path d="M3.5 3h1.6l.6 1.6-.9.7a4.5 4.5 0 0 0 1.9 1.9l.7-.9 1.6.6V8.5c0 .4-.3.6-.7.6A5.6 5.6 0 0 1 3 3.7c0-.4.2-.7.5-.7z" fill="#111"/></svg>
        000-000-0000
      </li>
      <li class="contact__item">
        <svg class="contact__icon" viewBox="0 0 12 12"><rect width="12" height="12" rx="2" fill="var(--accent)"/><rect x="2.5" y="3.5" width="7" height="5" fill="none" stroke="#111" stroke-width="1"/><path d="M2.5 3.5 6 6.5l3.5-3" fill="none" stroke="#111" stroke-width="1"/></svg>
        jr@maetech.com
      </li>
      <li class="contact__item">
        <svg class="contact__icon" viewBox="0 0 12 12"><rect width="12" height="12" rx="2" fill="var(--accent)"/><circle cx="6" cy="6" r="3.4" fill="none" stroke="#111" stroke-width="1"/><path d="M2.6 6h6.8M6 2.6c-1.6 2-1.6 4.8 0 6.8M6 2.6c1.6 2 1.6 4.8 0 6.8" fill="none" stroke="#111" stroke-width=".8"/></svg>
        www.maetech.com
      </li>
    </ul>

    <p class="person">JORDAN REYES</p>
  </section>

  <section class="card card--back" aria-label="Business card back">
    <div class="brand">
      <span class="brand__dot"></span>
      <span class="brand__name">MAE TECHNOLOGIES</span>
    </div>
    <span class="brand__tagline">Marlow Alarm &amp; Egress</span>

    <div class="services">
      <p>Installation of:</p>
      <p>Fire Detection and Emergency Warning Systems</p>
      <p>Comprehensive maintenance of all Fire Protection and prevention equipment and systems.</p>
      <p class="services__callout">24/7 ON CALL MAINTENANCE</p>
    </div>
  </section>
</body>
</html>
```